Vornel Technologies business card design

We need a business card designed with our new logo. it would be great if the card could communicate it is a technology based company.

Target Market(s)

system integrators

Industry/Entity Type

technology, IOT

Contact Information for Business Card

Name, designation, Address, telephone number, email address

Requirements
Must have
• logo and company name
Nice to have
• something to do with technology

```html
<!DOCTYPE html>
<html lang="en">
<head>
<meta charset="utf-8">
<title>Vornel Technologies – Business Card</title>
<link href="https://fonts.googleapis.com/css2?family=Roboto:wght@400;500&display=swap" rel="stylesheet">
<style>
  :root{
    --orange:#e8902a;
    --orange-light:#ea9a30;
    --orange-deep:#e3861d;
    --ink:#3d3e42;
    --text:#46474b;
    --card:#f7f7f8;
    --page:#e4e4e4;
    --white:#ffffff;
  }
  *{margin:0;padding:0;box-sizing:border-box;}
  html,body{width:1200px;height:1200px;overflow:hidden;background:var(--page);}
  body{font-family:"Roboto",Arial,sans-serif;position:relative;}

  .card{
    position:absolute;left:200px;width:800px;height:457px;
    border-radius:24px;overflow:hidden;
  }
  .card--front{top:60px;background:var(--card);}
  .card--back{top:630px;background:linear-gradient(180deg,var(--orange-light),var(--orange-deep));}

  .wordmark{
    position:absolute;left:0;right:0;
    display:flex;align-items:center;justify-content:center;gap:22px;
    font-weight:500;
  }
  .wordmark__square{width:64px;height:64px;background:currentColor;flex:none;}
  .wordmark__text{display:flex;flex-direction:column;line-height:1;}
  .wordmark__name{font-size:64px;letter-spacing:1px;}
  .wordmark__sub{font-size:22px;letter-spacing:9.6px;margin-top:10px;}
  .card--front .wordmark{top:100px;color:var(--ink);}
  .card--front .wordmark__square{background:var(--orange);}
  .card--back .wordmark{top:180px;color:var(--white);}

  .person{
    position:absolute;right:410px;top:274px;text-align:right;color:var(--text);
    font-size:17px;line-height:22px;
  }
  .person__name{color:var(--orange);font-size:27px;font-weight:500;line-height:32px;margin-bottom:6px;}
  .person__role{margin-bottom:8px;}

  .divider{position:absolute;left:413px;top:272px;width:1px;height:118px;background:#cfcfd2;}

  .contact{
    position:absolute;left:432px;top:286px;list-style:none;color:var(--text);
    font-size:17px;line-height:22.5px;
  }
  .contact li{display:flex;align-items:center;gap:10px;}
  .contact svg{width:16px;height:16px;flex:none;fill:var(--orange);}

  .band{position:absolute;bottom:0;height:14px;}
  .band--orange{left:0;width:400px;background:var(--orange);}
  .band--ink{left:402px;right:0;background:var(--ink);}
</style>
</head>
<body>

<section class="card card--front" aria-label="Card front">
  <div class="wordmark">
    <span class="wordmark__square"></span>
    <span class="wordmark__text">
      <span class="wordmark__name">VORNEL</span>
      <span class="wordmark__sub">TECHNOLOGIES</span>
    </span>
  </div>

  <div class="person">
    <p class="person__name">Daniel Morrow</p>
    <p class="person__role">Managing Director</p>
    <p>1420 Linden Court</p>
    <p>Juneau, Alaska 34812</p>
  </div>

  <div class="divider"></div>

  <ul class="contact">
    <li>
      <svg viewBox="0 0 16 16" aria-hidden="true"><path d="M3.2 1.5l2.3 2.6-1.3 1.8c.9 2 2.4 3.5 4.4 4.4l1.8-1.3 2.6 2.3-1.2 2.2C6.9 14.8 1.2 9.1 1 3.4z"/></svg>
      555-210-4786
    </li>
    <li>
      <svg viewBox="0 0 16 16" aria-hidden="true"><path d="M4.5 0.5h7v15h-7zM5.8 2v10.5h4.4V2zM7.3 13.3h1.4v1.2H7.3z" fill-rule="evenodd"/></svg>
      555-318-9042
    </li>
    <li>
      <svg viewBox="0 0 16 16" aria-hidden="true"><path d="M1 3.5h14v9H1zM2.3 4.5L8 8.8l5.7-4.3zM2 5.7v5.8l3.8-3zM14 5.7l-3.8 2.8 3.8 3z" fill-rule="evenodd"/></svg>
      info@vornel.com
    </li>
    <li>
      <svg viewBox="0 0 16 16" aria-hidden="true"><circle cx="8" cy="8" r="7"/><path d="M4 4.5c1.5.2 2.4 1.2 2 2.5-.5 1.3.6 2 1.6 2.3.8.3.5 2-.3 3.2M10 2.3c-.5 1.3.4 2.4 1.8 2.3 1 0 1.6 1 1.3 2" fill="none" stroke="#f7f7f8" stroke-width="1.1"/></svg>
      www.vornel.com
    </li>
  </ul>

  <div class="band band--orange"></div>
  <div class="band band--ink"></div>
</section>

<section class="card card--back" aria-label="Card back">
  <div class="wordmark">
    <span class="wordmark__square"></span>
    <span class="wordmark__text">
      <span class="wordmark__name">VORNEL</span>
      <span class="wordmark__sub">TECHNOLOGIES</span>
    </span>
  </div>
</section>

</body>
</html>
```